Architecture firm needing a business card

We need a business card design for a new company based in the US called "Pellmore Architecture". Seeking minimalist designs that have a creativity/design feel but must be clean and professional. Please refer to the logo attached.

Target Market(s)

Real Estate Investors, Home Builders and Construction Firms.

Industry/Entity Type

Architecture

Contact Information for Business Card

Standard US size business cards. Would like to have some sort of graphic on the back side of the card - nothing that is too loud but something that may catch your attention. More or less grayscale colors that are in line with the logo colors (navy and greys essentially). Additional colors maybe accepted if blended properly (earthtones), but might be difficult to accomplish and maintain the clean/minimalist look.

Requirements
Must have
• Clean Lines
Nice to have
• some sort of graphics, would like to have something creative on the back side of the card
Should not have
• nothing too busy, cluttered or overwhelming.

```html
<!DOCTYPE html>
<html lang="en">
<head>
<meta charset="utf-8">
<title>Pellmore Architecture – Business Card</title>
<link href="https://fonts.googleapis.com/css2?family=Open+Sans:ital,wght@0,400;0,600;0,700;1,400&display=swap" rel="stylesheet">
<style>
  :root {
    --navy: #1b3f69;
    --grey: #8c8c8c;
    --paper: #ffffff;
    --backdrop: #d9d9d9;
    --card-w: 620px;
    --card-h: 354px;
  }
  * { box-sizing: border-box; margin: 0; padding: 0; }
  html, body {
    width: 1200px; height: 900px; overflow: hidden;
    background: var(--backdrop);
    font-family: "Open Sans", Arial, sans-serif;
  }
  .sheet {
    width: 1200px; height: 900px;
    display: flex; flex-direction: column;
    align-items: center; justify-content: center; gap: 40px;
  }
  .card {
    position: relative;
    width: var(--card-w); height: var(--card-h);
    background: var(--paper);
    box-shadow: 0 6px 18px rgba(0,0,0,0.12);
    overflow: hidden;
  }
  /* Front */
  .person { position: absolute; left: 52px; top: 82px; }
  .person-name {
    color: var(--navy); font-weight: 700; font-size: 30px;
    letter-spacing: -0.5px; line-height: 1;
  }
  .person-title {
    color: var(--grey); font-style: italic; font-size: 14px; line-height: 1.2;
  }
  .phones { position: absolute; left: 52px; top: 170px; }
  .contact-row {
    display: flex; align-items: center; gap: 10px;
    color: var(--navy); font-style: italic; font-weight: 600; font-size: 12px;
    line-height: 18px;
  }
  .contact-row svg { width: 10px; height: 10px; fill: var(--navy); flex: none; }
  .brand {
    position: absolute; left: 330px; top: 92px;
    display: flex; align-items: center; gap: 12px;
  }
  .brand-mark { width: 34px; height: 34px; background: var(--grey); }
  .brand-name {
    color: var(--navy); font-weight: 400; font-size: 20px;
    letter-spacing: 1.5px; text-transform: uppercase;
  }
  .web { position: absolute; left: 340px; top: 222px; }
  .band {
    position: absolute; left: 0; right: 0; bottom: 0; height: 66px;
    background: var(--navy);
    display: flex; align-items: center; padding-left: 150px; gap: 10px;
    color: var(--paper); font-style: italic; font-size: 13px;
  }
  .band svg { width: 11px; height: 11px; fill: var(--paper); }
  /* Back */
  .card-back { background: var(--navy); padding: 10px; }
  .back-pattern {
    width: 100%; height: 100%;
    background: linear-gradient(135deg, #244a76, #1b3f69 50%, #254c78);
    border: 2px solid rgba(255,255,255,0.55);
  }
</style>
</head>
<body>
<main class="sheet">
  <section class="card card-front" aria-label="Business card front">
    <div class="person">
      <p class="person-name">NAME</p>
      <p class="person-title">title/designation</p>
    </div>
    <div class="phones">
      <p class="contact-row">
        <svg viewBox="0 0 10 10"><path d="M2 0h2l1 3-1.5 1a6 6 0 0 0 2.5 2.5L7 5l3 1v2c0 1-1 2-2 2A8 8 0 0 1 0 2c0-1 1-2 2-2z"/></svg>
        +(000) 1234 5678
      </p>
      <p class="contact-row">
        <svg viewBox="0 0 10 10"><rect x="2" y="0" width="6" height="3"/><rect x="0" y="4" width="10" height="4"/><rect x="2" y="7" width="6" height="3"/></svg>
        +(000) 1234 5679
      </p>
    </div>
    <div class="brand">
      <span class="brand-mark" aria-hidden="true"></span>
      <span class="brand-name">Pellmore Architecture</span>
    </div>
    <div class="web">
      <p class="contact-row">
        <svg viewBox="0 0 10 10"><path d="M0 1h10v8H0z M1 2v.5l4 3 4-3V2z" fill-rule="evenodd"/></svg>
        hello@pellmorearchitecture.com
      </p>
      <p class="contact-row">
        <svg viewBox="0 0 10 10"><circle cx="5" cy="5" r="4.2" fill="none" stroke="#1b3f69" stroke-width="1.2"/><path d="M0.8 5h8.4M5 0.8v8.4" stroke="#1b3f69" stroke-width="0.9"/></svg>
        pellmorearchitecture.com
      </p>
    </div>
    <div class="band">
      <svg viewBox="0 0 10 10"><path d="M5 0a3.5 3.5 0 0 1 3.5 3.5C8.5 6 5 10 5 10S1.5 6 1.5 3.5A3.5 3.5 0 0 1 5 0zm0 2a1.5 1.5 0 1 0 0 3 1.5 1.5 0 0 0 0-3z" fill-rule="evenodd"/></svg>
      410 Marlowe Street, Brookfield 54321
    </div>
  </section>

  <section class="card card-back" aria-label="Business card back">
    <div class="back-pattern" role="img" aria-label="Repeating navy and white geometric interlocking pattern covering the card back"></div>
  </section>
</main>
</body>
</html>
```